Professional BBQ Cleaning Flyer (Before & After Focus)

We need a clean, professional double-sided A5 flyer for a BBQ cleaning business.
This flyer will be handed directly to:
Property managers
Retirement villages
Over 50s communities
Resorts / body corporate
The design must feel professional, trustworthy, and easy to read β not cluttered or cheap.
π― Goal
Use a strong before & after BBQ image to show the value of the service, and position the business as reliable for communal BBQ cleaning.
π Size & Format
A5 (148 x 210mm)
Portrait (vertical)
Double-sided
Print-ready (with bleed)
π¨ Style & Branding
Colours: Red, Black, White
Clean, modern, minimal
Strong, easy-to-read fonts (important for older audience)
Plenty of white space
No emojis, no clutter, no cheap design elements
π₯ FRONT SIDE (IMPORTANT β MAIN FOCUS)
Must include:
Headline:
Professional BBQ Cleaning
For Shared & Communal Areas
Subheadline:
Keep your BBQs clean, safe, and ready for residents & guests
Main Visual :
Side-by-side BEFORE & AFTER BBQ
This is the main focus of the flyer
Must be realistic and high quality
Labels under images:
BEFORE β Greasy β’ Dirty β’ Unsafe
AFTER β Clean β’ Hygienic β’ Ready to Use
Short Bullet Points:
Deep clean of grills, burners & internal components
Ideal for retirement villages, resorts & body corporate
Multiple BBQs cleaned in one visit
Trust Line:
Fully insured & police checked
Call to Action (bottom):
Get a Quote or Book a Service
0438 254 091
www.grillshinecrew.com.au
β¬ BACK SIDE (CREDIBILITY & DETAIL)
Headline:
Trusted by Property Managers & Facilities Teams
Whatβs Included:
Full dismantle and deep clean
Removal of grease, carbon & built-up residue
Grills, burners, trays & surfaces cleaned
Reassembled and checked
Why Choose Us:
Professional, reliable service
Works around your schedule
Ideal for high-use communal BBQ areas
One-off or ongoing maintenance
Ideal For:
Retirement villages
Apartment complexes
Resorts
Body corporate properties
Closing Line:
Keep your shared BBQ areas clean, safe, and presentable year-round
Contact:
Grill Shine Crew
0438 254 091
www.grillshinecrew.com.au
grillshinecrew@mailbox-demo.com.au

```html
<!DOCTYPE html>
<html lang="en">
<head>
<meta charset="utf-8">
<title>Grill Shine Crew – BBQ Cleaning Flyer</title>
<link href="https://fonts.googleapis.com/css2?family=Montserrat:wght@700;800&family=Poppins:wght@400;500;600;700&display=swap" rel="stylesheet">
<style>
  :root{
    --red:#d02a3c;
    --black:#050505;
    --white:#ffffff;
    --ink:#141414;
    --grey:#5a5a5a;
    --soft-pink:#fcd4d8;
    --line:#bdbdbd;
    --stage:#d9d9d9;
    --foot-text:#d8d8d8;
  }
  *{margin:0;padding:0;box-sizing:border-box}
  html,body{width:704px;height:1200px;overflow:hidden;background:var(--stage)}
  body{font-family:"Poppins",sans-serif;color:var(--ink);position:relative}
  .flyer{position:absolute;left:152px;width:400px;height:567px;background:var(--white);overflow:hidden}
  .flyer--front{top:22px}
  .flyer--back{top:611px}
  .abs{position:absolute}
  .tick{width:10px;height:10px;flex:none}

  /* FRONT */
  .brand{top:16px;left:0;width:100%;display:flex;justify-content:center;align-items:center;gap:7px}
  .brand__dot{width:22px;height:22px;border-radius:50%;background:var(--red)}
  .brand__name{font-family:"Poppins",sans-serif;font-weight:700;font-size:17px;color:var(--black)}
  .headline{top:70px;width:100%;text-align:center;font-family:"Montserrat",sans-serif;font-weight:800;font-size:30px;line-height:31px;color:var(--black)}
  .headline__sub{top:137px;width:100%;text-align:center;font-family:"Montserrat",sans-serif;font-weight:700;font-size:17px;color:var(--red)}
  .rule{top:162px;left:41px;width:318px;height:1px;background:var(--grey)}
  .subhead{top:167px;width:100%;text-align:center;font-size:13.5px;line-height:17px;font-weight:500}
  .photo{top:217px;height:140px}
  .photo--before{left:0;width:197px;background:radial-gradient(ellipse at 45% 55%,#8a5a22 0%,#4a2e12 45%,#1c130b 100%)}
  .photo--after{left:202px;width:198px;background:linear-gradient(180deg,#9a9a9a 0%,#4a4a4a 35%,#1a1a1a 100%)}
  .label{top:357px;height:40px;text-align:center;color:var(--white);padding-top:4px}
  .label--before{left:0;width:197px;background:var(--black)}
  .label--after{left:202px;width:198px;background:var(--red)}
  .label__title{font-family:"Poppins",sans-serif;font-weight:700;font-size:14px;line-height:17px}
  .label__tags{font-size:9px;line-height:13px}
  .points{top:405px;left:24px;list-style:none}
  .points li{display:flex;align-items:center;gap:5px;font-size:11.5px;font-weight:600;height:21px}
  .cta-band{top:473px;left:0;width:400px;height:27px;background:var(--soft-pink);padding-left:24px;font-size:15px;font-weight:600;line-height:27px}
  .contact-band{top:500px;left:0;width:400px;height:67px;background:var(--black)}
  .phone{top:7px;left:24px;display:flex;align-items:center;gap:9px}
  .phone__icon{width:29px;height:29px}
  .phone__num{font-family:"Montserrat",sans-serif;font-weight:800;font-size:32px;color:var(--white);line-height:36px}
  .web{top:44px;left:24px;font-size:13px;letter-spacing:2.2px;color:var(--white)}
  .badge{top:449px;left:284px;width:90px;height:90px}
  .badge__ray{position:absolute;left:10px;top:10px;width:70px;height:70px;background:var(--red)}
  .badge__text{position:absolute;inset:0;display:flex;align-items:center;justify-content:center;text-align:center;font-family:"Poppins",sans-serif;font-weight:700;font-size:11.5px;line-height:14px;color:var(--white)}

  /* BACK */
  .back-head{top:0;left:0;width:400px;height:85px;background:var(--red);padding:26px 23px 0;font-family:"Montserrat",sans-serif;font-weight:800;font-size:20.5px;line-height:25px;color:var(--white)}
  .section{left:23px}
  .section__title{font-weight:700;font-size:13px;line-height:16px;color:var(--black)}
  .list{list-style:none;margin-top:2px}
  .list li{display:flex;gap:6px;font-size:13px;line-height:19.5px}
  .list li .tick{margin-top:5px}
  .list--tight li{line-height:14px;margin-bottom:5.5px}
  .list--tight li .tick{margin-top:2px}
  .dots{left:0;width:400px;border-top:1px dotted #f2a8b0}
  .ideal{top:368px;left:23px;width:351px;height:63px;border:1.3px dashed var(--line);border-radius:6px;display:flex;padding-top:8px}
  .ideal__tag{top:358px;left:23px;height:19px;padding:0 9px;background:#4d4d4d;color:var(--white);font-weight:700;font-size:13px;line-height:19px}
  .ideal__item{font-size:12px;line-height:13.5px;padding:4px 0 0 10px;border-right:1.3px solid var(--line);height:43px}
  .ideal__item:last-child{border-right:none}
  .back-foot{top:442px;left:0;width:400px;height:125px;background:var(--black)}
  .closing{top:11px;left:23px;width:340px;font-size:13px;line-height:16.5px;color:var(--foot-text)}
  .foot-brand{top:70px;left:23px;display:flex;align-items:center;gap:6px}
  .foot-brand .brand__dot{width:18px;height:18px}
  .foot-brand .brand__name{color:var(--white);font-size:12.5px;line-height:14px;width:70px}
  .foot-divider{top:57px;left:137px;width:1px;height:55px;background:var(--foot-text)}
  .foot-contact{top:52px;left:152px}
  .foot-contact__phone{font-family:"Montserrat",sans-serif;font-weight:800;font-size:27px;line-height:30px;color:var(--white)}
  .foot-contact__web{font-size:12px;line-height:13px;color:var(--white)}
  .foot-contact__mail{font-size:11px;line-height:13px;color:var(--red)}
</style>
</head>
<body>
<svg width="0" height="0" style="position:absolute">
  <symbol id="tick" viewBox="0 0 20 20">
    <circle cx="10" cy="10" r="8.3" fill="none" stroke="#d02a3c" stroke-width="2"/>
    <path d="M6 10.3l2.8 2.8L14.4 7" fill="none" stroke="#d02a3c" stroke-width="2.2" stroke-linecap="round" stroke-linejoin="round"/>
  </symbol>
</svg>

<!-- FRONT SIDE -->
<section class="flyer flyer--front">
  <div class="abs brand"><span class="brand__dot"></span><span class="brand__name">Grill Shine Crew</span></div>
  <h1 class="abs headline">Professional<br>BBQ Cleaning</h1>
  <h2 class="abs headline__sub">For Shared &amp; Communal Areas</h2>
  <div class="abs rule"></div>
  <p class="abs subhead">Keep your BBQs clean, safe, and ready<br>for residents &amp; guests</p>

  <div class="abs photo photo--before" role="img" aria-label="Photo of a greasy, carbon-covered BBQ grill before cleaning"></div>
  <div class="abs photo photo--after" role="img" aria-label="Photo of the same BBQ grill shining clean after cleaning"></div>
  <div class="abs label label--before"><div class="label__title">BEFORE</div><div class="label__tags">Greasy • Dirty • Unsafe</div></div>
  <div class="abs label label--after"><div class="label__title">AFTER</div><div class="label__tags">Clean • Hygienic • Ready to Use</div></div>

  <ul class="abs points">
    <li><svg class="tick"><use href="#tick"/></svg>Deep clean of grills, burners &amp; internal components</li>
    <li><svg class="tick"><use href="#tick"/></svg>Ideal for retirement villages, resorts &amp; body corporate</li>
    <li><svg class="tick"><use href="#tick"/></svg>Multiple BBQs cleaned in one visit</li>
  </ul>

  <div class="abs cta-band">Get a Quote or Book a Service</div>
  <div class="abs contact-band">
    <div class="abs phone">
      <svg class="phone__icon" viewBox="0 0 30 30">
        <circle cx="15" cy="15" r="14" fill="#d02a3c"/>
        <path d="M10.5 8.5c.6-.6 1.5-.6 2 0l1.6 2c.4.5.4 1.2 0 1.7l-.9 1c.8 1.6 2 2.8 3.6 3.6l1-.9c.5-.4 1.2-.4 1.7 0l2 1.6c.6.5.6 1.4 0 2l-1.2 1.2c-.9.9-2.3 1.1-3.4.5-3.3-1.7-5.9-4.3-7.6-7.6-.6-1.1-.4-2.5.5-3.4z" fill="#fff"/>
      </svg>
      <span class="phone__num">0438 254 091</span>
    </div>
    <div class="abs web">www.grillshinecrew.com.au</div>
  </div>

  <div class="abs badge">
    <span class="badge__ray"></span>
    <span class="badge__ray" style="transform:rotate(22.5deg)"></span>
    <span class="badge__ray" style="transform:rotate(45deg)"></span>
    <span class="badge__ray" style="transform:rotate(67.5deg)"></span>
    <span class="badge__text">FULLY<br>INSURED<br>&amp; POLICE<br>CHECKED</span>
  </div>
</section>

<!-- BACK SIDE -->
<section class="flyer flyer--back">
  <h1 class="abs back-head">Trusted by Property Managers<br>&amp; Facilities Teams</h1>

  <div class="abs section" style="top:104px">
    <h3 class="section__title">WHAT’S INCLUDED</h3>
    <ul class="list list--tight" style="margin-top:4px">
      <li><svg class="tick"><use href="#tick"/></svg>Full dismantle and deep clean</li>
      <li><svg class="tick"><use href="#tick"/></svg>Removal of grease, carbon &amp; built-up residue</li>
      <li><svg class="tick"><use href="#tick"/></svg><span>Grills, burners, trays &amp; surfaces cleaned<br>Reassembled and checked</span></li>
    </ul>
  </div>
  <div class="abs dots" style="top:207px"></div>

  <div class="abs section" style="top:219px">
    <h3 class="section__title">WHY CHOOSE US</h3>
    <ul class="list">
      <li><svg class="tick"><use href="#tick"/></svg>Professional, reliable service</li>
      <li><svg class="tick"><use href="#tick"/></svg>Works around your schedule</li>
      <li><svg class="tick"><use href="#tick"/></svg>Ideal for high-use communal BBQ areas</li>
      <li><svg class="tick"><use href="#tick"/></svg>One-off or ongoing maintenance</li>
      <li><svg class="tick"><use href="#tick"/></svg>Fully insured &amp; police checked</li>
    </ul>
  </div>
  <div class="abs dots" style="top:348px"></div>

  <div class="abs ideal">
    <div class="ideal__item" style="width:87px">Retirement<br>villages</div>
    <div class="ideal__item" style="width:88px">Apartment<br>complexes</div>
    <div class="ideal__item" style="width:69px">Resorts</div>
    <div class="ideal__item" style="width:105px">Body corporate<br>properties</div>
  </div>
  <div class="abs ideal__tag">Ideal For</div>

  <footer class="abs back-foot">
    <p class="abs closing">Keep your shared BBQ areas clean, safe, and presentable year-round</p>
    <div class="abs foot-brand"><span class="brand__dot"></span><span class="brand__name">Grill Shine Crew</span></div>
    <div class="abs foot-divider"></div>
    <div class="abs foot-contact">
      <div class="foot-contact__phone">0438 254 091</div>
      <div class="foot-contact__web">www.grillshinecrew.com.au</div>
      <div class="foot-contact__mail">grillshinecrew@mailbox-demo.com.au</div>
    </div>
  </footer>
</section>
</body>
</html>
```